landing and results page for local search engine for childrens stuff

wimbro.it is local search engine to find children clothes, bikes, toys, etc locally.

we search thousands of sites tradlo, swapnest and many more to bring together millions of ads so you can find them all in one place, and organize them with useful features so parents can find local bargains for kids stuff.

the key here is we specialise in finding kids gear, and only bring you results that are local to the user.
look and feel something like this http://www.plinvo.com/
and http://www.tesk.com/

Target Market(s)

mums, parents , people with kids

Industry/Entity Type

Tradlo

Requirements
Must have
• it must convey that this is a location aware search engine for kids stuff. an image similar to this http://www.brambolapp.com/
on landing page

```html
<!DOCTYPE html>
<html lang="en">
<head>
<meta charset="utf-8">
<title>wimbro.it — local kids gear search</title>
<link rel="stylesheet" href="https://fonts.googleapis.com/css2?family=Kalam:wght@400;700&family=Arimo:ital,wght@0,400;0,700;1,400&display=swap">
<style>
  :root {
    --green: #00c988;
    --green-deep: #006a45;
    --green-ink: #0b4a2c;
    --cream: #fff0a6;
    --orange: #f7931e;
    --orange-light: #ffab3d;
    --orange-deep: #e07700;
    --field: #ffffff;
    --field-text: #8a8a8a;
    --hint: #2b2b2b;
    --btn-dark: #083a26;
    --map-light: #f3e6bd;
    --map-mid: #d9bd82;
  }
  * { box-sizing: border-box; margin: 0; padding: 0; }
  html, body { width: 1200px; height: 1000px; overflow: hidden; }
  body {
    position: relative;
    background: var(--cream);
    font-family: "Arimo", Arial, sans-serif;
  }

  /* header */
  .site-header { position: absolute; left: 0; top: 0; width: 1200px; height: 120px; }
  .site-header svg { position: absolute; inset: 0; }
  .brand {
    position: absolute; left: 0; right: 0; top: 18px;
    display: flex; justify-content: center; align-items: center; gap: 12px;
    font-family: "Kalam", cursive; font-weight: 700; font-size: 52px;
    color: var(--orange); line-height: 1;
  }
  .brand-dot { width: 26px; height: 26px; border-radius: 50%; background: var(--orange); }
  .account { position: absolute; top: 0; right: 185px; display: flex; gap: 8px; }
  .account a {
    display: block; padding: 0 16px; height: 42px; line-height: 42px;
    font-weight: 700; font-size: 17px; color: #fff; text-decoration: none;
    border-radius: 0 0 4px 4px;
  }
  .account .join { background: linear-gradient(var(--orange-light), var(--orange-deep)); }
  .account .login { background: var(--btn-dark); }

  /* search */
  .search-labels {
    position: absolute; top: 180px; left: 193px; width: 840px;
    font-family: "Kalam", cursive; font-size: 29px; line-height: 36px; color: var(--orange);
  }
  .search-labels span { position: absolute; white-space: nowrap; }
  .search-labels .where { left: 419px; }
  .search-bar {
    position: absolute; left: 161px; top: 224px; width: 874px; height: 82px;
    background: var(--green); border-radius: 8px;
  }
  .field {
    position: absolute; top: 19px; height: 44px; background: var(--field);
    border-radius: 5px; box-shadow: inset 0 1px 3px rgba(0,0,0,.25);
  }
  .field span { position: absolute; left: 14px; top: 13px; font-size: 16px; color: var(--field-text); }
  .field .drop {
    position: absolute; right: 0; top: 0; width: 44px; height: 44px;
    background: var(--btn-dark); border-radius: 0 5px 5px 0;
    display: flex; align-items: center; justify-content: center;
  }
  .field.what { left: 20px; width: 314px; }
  .field.where { left: 365px; width: 315px; }
  .search-bar .go {
    position: absolute; left: 708px; top: 18px; width: 148px; height: 46px;
    background: linear-gradient(var(--orange-light), var(--orange-deep));
    border-radius: 4px; color: #fff;
    font-family: "Kalam", cursive; font-size: 28px; text-align: center; line-height: 50px;
  }
  .hint { position: absolute; top: 318px; font-size: 12px; font-style: italic; color: var(--hint); }
  .hint.what { left: 197px; }
  .hint.where { left: 543px; }

  /* hero */
  .tagline {
    position: absolute; left: 197px; top: 396px;
    font-family: "Kalam", cursive; font-weight: 400; font-size: 30px; line-height: 40px;
    color: var(--green-ink);
  }
  .hero-art {
    position: absolute; left: 480px; top: 405px; width: 540px; height: 290px;
    border-radius: 50%;
    background: radial-gradient(ellipse at 50% 55%, var(--map-light) 0%, var(--map-mid) 45%, rgba(255,240,166,0) 72%);
  }

  /* footer */
  .site-footer { position: absolute; left: 0; top: 700px; width: 1200px; height: 300px; }
  .site-footer svg { position: absolute; inset: 0; }
  .footer-col { position: absolute; top: 157px; font-size: 14px; line-height: 19.5px; color: var(--green-ink); }
  .footer-col h3 {
    font-family: "Kalam", cursive; font-weight: 700; font-size: 18px; line-height: 22px; margin-bottom: 2px;
  }
  .footer-col ul { list-style: none; }
  .footer-col.nav { left: 417px; }
  .footer-col.legal { left: 530px; top: 181px; }
  .footer-col.social { left: 719px; top: 160px; }
</style>
</head>
<body>

<header class="site-header">
  <svg width="1200" height="120" viewBox="0 0 1200 120" aria-hidden="true">
    <defs>
      <linearGradient id="headerBand" x1="0" x2="1" y1="0" y2="0">
        <stop offset="0" stop-color="var(--green-deep)"/>
        <stop offset="0.5" stop-color="var(--green)"/>
        <stop offset="1" stop-color="var(--green-deep)"/>
      </linearGradient>
    </defs>
    <path d="M0 0H1200V62C1000 58 820 110 600 108C380 106 200 60 0 64Z" fill="url(#headerBand)"/>
  </svg>
  <div class="brand"><span class="brand-dot"></span>wimbro.it</div>
  <nav class="account">
    <a class="join" href="#">Join</a>
    <a class="login" href="#">Login</a>
  </nav>
</header>

<main>
  <div class="search-labels">
    <span class="what">What would you like?</span>
    <span class="where">Where?</span>
  </div>
  <form class="search-bar">
    <div class="field what"><span>type a category or keyword</span>
      <div class="drop"><svg width="18" height="12" viewBox="0 0 18 12"><path d="M0 0H18L9 12Z" fill="var(--orange)"/></svg></div>
    </div>
    <div class="field where"><span>type a location</span>
      <div class="drop"><svg width="18" height="12" viewBox="0 0 18 12"><path d="M0 0H18L9 12Z" fill="var(--orange)"/></svg></div>
    </div>
    <div class="go">Search</div>
  </form>
  <p class="hint what">e.g. clothes, toy, book</p>
  <p class="hint where">e.g. boston, dallas, ca</p>

  <h2 class="tagline">Buy and sell with<br>local friendly people</h2>

  <div class="hero-art" role="img" aria-label="Illustration of an open town map with location pins, surrounded by kids' items: a rocking horse, abacus, football, books, shoes and a compass"></div>
</main>

<footer class="site-footer">
  <svg width="1200" height="300" viewBox="0 0 1200 300" aria-hidden="true">
    <defs>
      <linearGradient id="footerBand" x1="0" x2="1" y1="0" y2="0">
        <stop offset="0" stop-color="var(--green-deep)"/>
        <stop offset="0.5" stop-color="var(--green)"/>
        <stop offset="1" stop-color="var(--green-deep)"/>
      </linearGradient>
    </defs>
    <path d="M0 18C200 10 360 40 600 42C840 44 1000 12 1200 16V300H0Z" fill="url(#footerBand)"/>
  </svg>
  <div class="footer-col nav">
    <h3>Navigation</h3>
    <ul><li>Browse</li><li>We're Hiring</li><li>How It Works</li><li>Safety</li></ul>
  </div>
  <div class="footer-col legal">
    <ul><li>Terms of Service</li><li>Privacy Policy</li><li>Marketplace Rules</li><li>Help</li></ul>
  </div>
  <div class="footer-col social">
    <h3>Social</h3>
    <ul><li>Flitter</li><li>Friendbook</li><li>Globeplus</li><li>Pinboardly</li></ul>
  </div>
</footer>

</body>
</html>
```